Terra Swift Business Card Design

We need to improve the design of our current business card. We are a erosion control, hydro seeding company that serves many markets. We are attaching the current business card and our logo as reference. You may also visit our site at www.terraswiftllc.example to reference.

```html
<!DOCTYPE html>
<html lang="en">
<head>
<meta charset="utf-8">
<title>Terra Swift Business Card</title>
<link href="https://fonts.googleapis.com/css2?family=Roboto:wght@400;500;700;900&display=swap" rel="stylesheet">
<style>
  :root {
    --page: #d2d3d5;
    --paper: #ffffff;
    --green: #2ba56e;
    --green-soft: #4fb886;
    --ink: #1d1d1d;
    --white: #ffffff;
  }
  html, body { margin: 0; padding: 0; }
  body {
    width: 900px; height: 1200px; overflow: hidden;
    background: var(--page);
    font-family: "Roboto", Arial, sans-serif;
    color: var(--ink);
    position: relative;
  }
  .card {
    position: absolute; left: 135px; width: 631px;
    background: var(--paper);
    overflow: hidden;
  }
  .card--front { top: 215px; height: 357px; }
  .card--back { top: 628px; height: 360px; }

  .brand { position: absolute; display: flex; align-items: center; gap: 10px; }
  .brand__name { font-weight: 900; color: var(--green); white-space: nowrap; letter-spacing: -0.5px; }
  .brand__dot { border-radius: 50%; background: var(--green); flex: none; }
  .card--front .brand { left: 0; right: 0; top: 62px; justify-content: center; }
  .card--front .brand__name { font-size: 50px; }
  .card--front .brand__dot { width: 30px; height: 30px; }
  .card--back .brand { left: 28px; top: 52px; }
  .card--back .brand__name { font-size: 31px; }
  .card--back .brand__dot { width: 20px; height: 20px; }

  .rule { position: absolute; left: 0; right: 0; height: 6px; background: var(--ink); }
  .band { position: absolute; left: 0; right: 0; bottom: 0; background: var(--green); color: var(--white); }
  .card--front .rule { top: 194px; }
  .card--front .band { top: 200px; }
  .card--back .rule { top: 254px; height: 5px; }
  .card--back .band { top: 259px; }

  .markets { display: flex; justify-content: space-between; padding: 15px 20px 0 28px; }
  .market { width: 88px; text-align: center; }
  .market__icon { width: 62px; height: 66px; margin: 0 auto; background: var(--green-soft); border-radius: 4px; }
  .market__label { margin-top: 6px; font-size: 15px; font-weight: 700; line-height: 20px; white-space: nowrap; }

  .office { position: absolute; right: 28px; top: 43px; text-align: right; font-size: 15px; line-height: 21px; }
  .office__title { font-weight: 500; }
  .contact { position: absolute; right: 26px; text-align: right; font-size: 15px; }
  .contact__row { display: flex; justify-content: flex-end; align-items: center; gap: 5px; height: 21px; }
  .contact__row svg { width: 14px; height: 14px; fill: var(--green); flex: none; }
  .contact--phones { top: 132px; }
  .contact--phones .contact__row { height: 23px; }
  .contact--web { top: 185px; }

  .person { position: absolute; left: 28px; top: 182px; }
  .person__name { font-size: 21px; font-weight: 700; color: var(--green); text-transform: uppercase; line-height: 24px; }
  .person__role { font-size: 15px; line-height: 20px; }

  .services { text-align: center; padding-top: 6px; }
  .services__title { font-size: 20px; font-weight: 500; line-height: 26px; }
  .services__row { font-size: 15px; font-weight: 700; letter-spacing: 0.3px; line-height: 21px; margin-top: 2px; }
  .services__row:first-of-type { margin-top: 6px; }
</style>
</head>
<body>

<section class="card card--front">
  <div class="brand">
    <span class="brand__name">Terra Swift Solutions</span>
    <span class="brand__dot"></span>
  </div>
  <div class="rule"></div>
  <div class="band">
    <ul class="markets" style="list-style:none;margin:0;">
      <li class="market"><div class="market__icon" role="img" aria-label="Line icon of solar panels under a sun"></div><div class="market__label">Utility-scale<br>Solar</div></li>
      <li class="market"><div class="market__icon" role="img" aria-label="Line icon of a pickaxe at a rock face"></div><div class="market__label">Mine<br>Sites</div></li>
      <li class="market"><div class="market__icon" role="img" aria-label="Line icon of a gas pipeline valve"></div><div class="market__label">Natural<br>Gas</div></li>
      <li class="market"><div class="market__icon" role="img" aria-label="Line icon of power transmission towers"></div><div class="market__label">Transmission<br>Lines</div></li>
      <li class="market"><div class="market__icon" role="img" aria-label="Line icon of a factory with smokestacks"></div><div class="market__label">Industrial<br>Plants</div></li>
      <li class="market"><div class="market__icon" role="img" aria-label="Line icon of a building under a crane"></div><div class="market__label">Private<br>Developments</div></li>
    </ul>
  </div>
</section>

<section class="card card--back">
  <div class="brand">
    <span class="brand__name">Terra Swift Solutions</span>
    <span class="brand__dot"></span>
  </div>

  <address class="office" style="font-style:normal;">
    <div class="office__title">Corporate Headquarters</div>
    <div>72 Marsh Creek Lane</div>
    <div>Riverbend, NC 28000</div>
  </address>

  <div class="contact contact--phones">
    <div class="contact__row">555-201-4470
      <svg viewBox="0 0 24 24"><path d="M6.6 10.8a15.1 15.1 0 0 0 6.6 6.6l2.2-2.2a1 1 0 0 1 1-.25 11.4 11.4 0 0 0 3.6.57 1 1 0 0 1 1 1V20a1 1 0 0 1-1 1A17 17 0 0 1 3 4a1 1 0 0 1 1-1h3.5a1 1 0 0 1 1 1c0 1.25.2 2.45.57 3.57a1 1 0 0 1-.25 1z"/></svg>
    </div>
    <div class="contact__row">555-201-8832
      <svg viewBox="0 0 24 24"><path d="M7 1h10a2 2 0 0 1 2 2v18a2 2 0 0 1-2 2H7a2 2 0 0 1-2-2V3a2 2 0 0 1 2-2zm0 3v14h10V4z"/></svg>
    </div>
  </div>

  <div class="person">
    <div class="person__name">Dale Whitmore</div>
    <div class="person__role">Chief Operating Officer</div>
  </div>

  <div class="contact contact--web">
    <div class="contact__row">dalew@terraswiftllc.example
      <svg viewBox="0 0 24 24"><path d="M2 5h20v14H2zm2 2v.5l8 5 8-5V7l-8 5z"/></svg>
    </div>
    <div class="contact__row">www.terraswiftllc.example
      <svg viewBox="0 0 24 24"><path d="M12 2a10 10 0 1 0 0 20 10 10 0 0 0 0-20zm0 2c.9 1.3 1.6 3 1.9 5h-3.8c.3-2 1-3.7 1.9-5zM4.3 14a8 8 0 0 1 0-4h3.8a17 17 0 0 0 0 4zm1 2h3.1c.3 1.3.8 2.5 1.4 3.6A8 8 0 0 1 5.3 16zm3.1-8H5.3a8 8 0 0 1 4.5-3.6C9.2 5.5 8.7 6.7 8.4 8zM12 20c-.9-1.3-1.6-3-1.9-5h3.8c-.3 2-1 3.7-1.9 5zm2.2-6H9.8a15 15 0 0 1 0-4h4.4a15 15 0 0 1 0 4zm.1 5.6c.6-1.1 1.1-2.3 1.4-3.6h3.1a8 8 0 0 1-4.5 3.6zM15.9 14a17 17 0 0 0 0-4h3.8a8 8 0 0 1 0 4z"/></svg>
    </div>
  </div>

  <div class="rule"></div>
  <div class="band services">
    <div class="services__title">Our Services</div>
    <div class="services__row">Erosion Control &nbsp;|&nbsp; Seeding &amp; Mulching &nbsp;|&nbsp; Hydroseeding &nbsp;|&nbsp; Compost Blankets</div>
    <div class="services__row">Site Prep &amp; Grading &nbsp;|&nbsp; Laydown Construction &amp; Restoration &nbsp;|&nbsp; Filter Sock</div>
  </div>
</section>

</body>
</html>
```